SunMeadow Yoga Website Design

Business Logo - attached
5 pages being:
Home
About
Classes
Blog
Contact

Would like Scrolling webpage and yoga symbols to be used.

Must have's being:
Easy to navigate, Text needs to be able to be edited/updated, Enquire Now Links, More Information Links, be a secure site, SEO,

Please refer to attached document for the information for the body of the website.

Target Market(s)

Educators, Community Service, Health and Wellbeing, Mental Health

Industry/Entity Type

Yoga

Coding

Coded - Design and coding required

Number of Pages Required

5+ page

Font styles to use
Other font styles liked:
• Bella Bold BC

Colors
0094D4
00A9DD
6FCCEA
C7EBF8
E9F6FB
6B429C
8869AF
B7A5CE
E3DAEB
F3F0F8

Requirements
Must have
• Easy to navigate, Text needs to be able to be edited/updated, Enquire Now Links, More Information Links, be a secure site, SEO,
Nice to have
• Scrolling webpage, yoga symbols

```html
<!DOCTYPE html>
<html lang="en">
<head>
<meta charset="utf-8">
<title>SunMeadow Yoga</title>
<link href="https://fonts.googleapis.com/css2?family=Kaushan+Script&family=Roboto:wght@400;500;700&display=swap" rel="stylesheet">
<style>
:root{
  --purple:#8869af;
  --purple-deep:#5a1fd1;
  --lilac:#e3daeb;
  --lilac-soft:#f3f0f8;
  --ink:#1c1c1c;
  --white:#ffffff;
  --black:#000000;
  --script:"Kaushan Script", cursive;
  --sans:"Roboto", Arial, sans-serif;
}
*{box-sizing:border-box;margin:0;padding:0}
html,body{width:1200px;height:2464px;overflow:hidden}
body{position:relative;background:var(--white);font-family:var(--sans);color:var(--ink)}
.abs{position:absolute}

/* header */
.site-header{position:absolute;left:0;top:0;width:1200px;height:82px;background:var(--white);z-index:3}
.brand-badge{position:absolute;left:112px;top:12px;width:142px;height:142px;border-radius:50%;background:var(--white);box-shadow:0 2px 10px rgba(0,0,0,.15);display:flex;align-items:center;justify-content:center;text-align:center;z-index:4}
.brand-badge span{font-family:var(--sans);font-weight:500;font-size:17px;line-height:20px;color:var(--purple)}
.main-nav a{position:absolute;top:32px;font-size:15.5px;color:var(--ink);text-decoration:none}
.btn{position:absolute;background:var(--purple);color:var(--white);border-radius:24px;display:flex;align-items:center;justify-content:center;font-size:20px;text-decoration:none}
.btn-contact{left:945px;top:21px;width:142px;height:42px}

/* hero */
.hero{position:absolute;left:0;top:82px;width:1200px;height:680px;overflow:hidden}
.hero-photo{position:absolute;inset:0;background:linear-gradient(180deg,#6d4a2a 0%,#9a7550 35%,#c8a880 70%,#b89468 100%)}
.hero-curve{position:absolute;left:0;top:0}
.hero-title{position:absolute;left:0;top:110px;width:1200px;text-align:center;font-family:var(--script);font-size:72px;color:var(--white);line-height:90px}
.hero-title em{font-style:normal;color:var(--purple-deep)}
.search{position:absolute;left:357px;top:227px;width:486px;height:43px;background:var(--white);border-radius:22px}
.search span{position:absolute;left:19px;top:14px;font-size:11px;color:#333}
.search-btn{left:345px;top:0;width:141px;height:43px;border-radius:22px;font-size:20px}
.search-btn svg{margin-right:8px}
.dots{position:absolute;left:578px;top:567px;display:flex;align-items:center;gap:4px}
.dots i{display:block;width:7px;height:7px;border-radius:50%;background:var(--white)}
.dots i.on{width:13px;height:13px;background:var(--purple-deep);margin-right:3px}

/* benefits */
.figure-seated{position:absolute;left:316px;top:770px;width:560px;height:694px;background:var(--lilac);opacity:.85;border-radius:120px 120px 60px 60px / 90px 90px 60px 60px}
.section-title{position:absolute;font-family:var(--script);font-size:40px;color:var(--black);white-space:nowrap}
.section-title em{font-style:normal;color:var(--purple-deep)}
.title-dots{position:absolute;display:flex;gap:5px}
.title-dots i{display:block;width:4px;height:4px;border-radius:50%;background:var(--purple-deep)}
.title-dots i.big{width:5px;height:5px}
.intro{position:absolute;left:230px;top:878px;width:740px;text-align:center;font-size:15.5px;line-height:26px}
.card-center{position:absolute;left:440px;top:960px;width:319px;height:418px;background:var(--white);border-radius:40px;box-shadow:0 6px 22px rgba(0,0,0,.12);overflow:hidden}
.card-center::after{content:"";position:absolute;left:70px;bottom:0;width:180px;height:4px;border-radius:4px 4px 0 0;background:var(--purple-deep)}
.col-title{position:absolute;font-family:var(--script);font-size:26px;color:var(--black);text-align:center;width:280px}
.benefit-list{position:absolute;list-style:none;font-size:15.5px;line-height:22px}
.benefit-list li{position:relative;padding-left:23px;margin-bottom:4px}
.benefit-list li::before{content:"";position:absolute;left:0;top:5px;width:8px;height:8px;border-radius:50%;border:2px solid var(--purple);background:var(--white);box-shadow:inset 0 0 0 2px var(--white);background-color:var(--purple)}

/* about */
.photo{position:absolute;border-radius:40px}
.photo-class{left:112px;top:1553px;width:450px;height:342px;background:linear-gradient(135deg,#3d3a3a 0%,#8f7b6c 45%,#c9b7a6 100%)}
.photo-pose{left:313px;top:1826px;width:303px;height:205px;background:linear-gradient(180deg,#d8dee0 0%,#c9d0d1 70%,#a8a39a 100%);border:0}
.figure-standing{position:absolute;left:1080px;top:1560px;width:107px;height:464px;background:var(--lilac);border-radius:50px 50px 20px 20px}
.about-text{position:absolute;left:648px;top:1639px;width:446px;font-size:15.5px;line-height:26px}
.about-text p{margin-bottom:12px}
.btn-read{left:648px;top:1977px;width:176px;height:42px}

/* footer */
.site-footer{position:absolute;left:0;top:2118px;width:1200px;height:346px;background:var(--black);color:var(--white)}
.footer-brand{position:absolute;left:112px;top:90px;width:158px;text-align:center;font-size:24px;font-weight:500;line-height:30px}
.footer-brand i{display:block;width:10px;height:10px;border-radius:50%;background:var(--white);margin:0 auto 10px}
.foot-head{position:absolute;top:50px;font-size:20px;font-weight:700}
.foot-list{position:absolute;top:93px;list-style:none;font-size:13.5px;line-height:22.3px}
.foot-list li{display:flex;align-items:center}
.foot-list svg{width:12px;margin-right:8px;flex:none}
.newsletter{position:absolute;left:850px;top:88px;width:237px;height:30px;border-bottom:1px solid var(--white);font-size:8px;display:flex;align-items:center}
.newsletter svg{margin-right:10px}
.social{position:absolute;top:146px;display:flex;gap:8px;left:853px}
.social i{display:block;width:20px;height:20px;border-radius:3px;background:var(--white)}
.footer-rule{position:absolute;left:0;top:296px;width:1200px;height:1px;background:#555}
.copyright{position:absolute;left:0;top:312px;width:1200px;text-align:center;font-size:13.5px}
</style>
</head>
<body>

<header class="site-header">
  <nav class="main-nav">
    <a style="left:531px">Home</a>
    <a style="left:611px">About</a>
    <a style="left:690px">Classes</a>
    <a style="left:782px">Blog</a>
    <a style="left:851px">Contact</a>
  </nav>
  <a class="btn btn-contact">Contact</a>
</header>
<div class="brand-badge"><span>SunMeadow<br>Yoga</span></div>

<section class="hero">
  <div class="hero-photo" role="img" aria-label="Woman holding a standing yoga pose in a warm brick-walled studio with a potted plant"></div>
  <h1 class="hero-title">Welcome to <em>SunMeadow</em> Yoga</h1>
  <div class="search">
    <span>Search....</span>
    <a class="btn search-btn"><svg width="12" height="12" viewBox="0 0 12 12"><circle cx="5" cy="5" r="3.5" fill="none" stroke="#fff" stroke-width="1.6"/><path d="M7.5 7.5L11 11" stroke="#fff" stroke-width="1.8"/></svg>Search</a>
  </div>
  <div class="dots"><i class="on"></i><i></i><i></i><i></i></div>
  <svg class="hero-curve" width="1200" height="680" viewBox="0 0 1200 680">
    <path d="M0 569 Q600 779 1200 569 L1200 680 L0 680 Z" fill="#fff"/>
    <path d="M0 569 Q600 779 1200 569" fill="none" stroke="#8869af" stroke-width="6"/>
  </svg>
</section>

<section class="benefits">
  <div class="figure-seated" role="img" aria-label="Faint silhouette of a person seated in a meditation pose"></div>
  <h2 class="section-title" style="left:503px;top:800px">Benefits of <em>Yoga</em></h2>
  <div class="title-dots" style="left:574px;top:857px"><i></i><i></i><i class="big"></i><i></i><i></i></div>
  <p class="intro">The benefits of yoga can last a lifetime. It is my aim &amp; passion to introduce yoga to kids of all ages and backgrounds so that they can not only experience the benefits of yoga but fall in love with the practice.</p>

  <div class="card-center"></div>

  <h3 class="col-title" style="left:126px;top:990px">Healthy minds</h3>
  <ul class="benefit-list" style="left:137px;top:1048px;width:255px">
    <li>Cultivates confidence and self-esteem</li>
    <li>Develops concentration and attention</li>
    <li>Helps relax and sleep better</li>
    <li>Clears the mind for better clarity and decision making</li>
    <li>Calms the nervous system</li>
    <li>Learns to cope with stressful situations</li>
    <li>Balances emotions</li>
  </ul>

  <h3 class="col-title" style="left:460px;top:990px">Healthy bodies</h3>
  <ul class="benefit-list" style="left:471px;top:1048px;width:270px">
    <li>Develops strong, flexible and healthy</li>
    <li>Promotes spinal alignment and good posture</li>
    <li>Builds energy and stamina</li>
    <li>Improves internal physical function -organs, digestion, elimination, circulation, and blood flow.</li>
    <li>Helps breathing and lung capacity</li>
    <li>Teaches the enjoyment of movement</li>
    <li>Works the ‘whole’ body</li>
  </ul>

  <h3 class="col-title" style="left:788px;top:990px">Healthy spirits</h3>
  <ul class="benefit-list" style="left:798px;top:1048px;width:270px">
    <li>Fosters creativity, expression and imagination</li>
    <li>Cultivates kindness to themselves and others</li>
    <li>Cultivates respect for self and others</li>
    <li>Builds balance and inner quiet</li>
    <li>Builds inner strength and resilience</li>
    <li>Teaches self-awareness</li>
    <li>Focuses on positive self-talk</li>
  </ul>
</section>

<section class="about">
  <div class="photo photo-class" role="img" aria-label="Group of women meditating cross-legged on mats in a bright loft studio"></div>
  <div class="photo photo-pose" role="img" aria-label="Woman in a low lunge yoga pose in a light room with plants"></div>
  <div class="figure-standing" role="img" aria-label="Faint silhouette of a person standing with arms raised overhead"></div>
  <h2 class="section-title" style="left:648px;top:1556px">About <em>Us</em></h2>
  <div class="title-dots" style="left:678px;top:1611px"><i></i><i></i><i class="big"></i><i></i><i></i></div>
  <div class="about-text">
    <p>Hi and welcome to SunMeadow Yoga!<br>My name is Hannah, and I am the creator &amp; facilitator of SunMeadow Yoga.</p>
    <p>With the increasing numbers of youth mental health, I have started SunMeadow Yoga wanting to assist children and teens with their mental health for life, with the magic of yoga.</p>
    <p>I genuinely believe the practice of yoga and mindfulness especially at a young age can offer life-long tools to kids and teens such as dealing with their emotions, developing resilience, self-awareness, respect and confidence in a positive and fun environment.</p>
  </div>
  <a class="btn btn-read">Read More</a>
</section>

<footer class="site-footer">
  <div class="footer-brand"><i></i>SunMeadow<br>Yoga</div>

  <h4 class="foot-head" style="left:376px">Address</h4>
  <ul class="foot-list" style="left:356px">
    <li><svg viewBox="0 0 12 12"><path d="M6 1a3.5 3.5 0 0 0-3.5 3.5C2.5 7 6 11 6 11s3.5-4 3.5-6.5A3.5 3.5 0 0 0 6 1z" fill="#fff"/><circle cx="6" cy="4.5" r="1.3" fill="#000"/></svg>Fernvale, Victoria Australia 3799</li>
    <li><svg viewBox="0 0 12 12"><path d="M3 1l2 2.5-1.2 1.2a7 7 0 0 0 3.5 3.5L8.5 7 11 9l-1.5 2C5 11 1 7 1 2.5z" fill="#fff"/></svg>0400 128 356</li>
    <li><svg viewBox="0 0 12 12"><rect x="1" y="3" width="10" height="7" fill="#fff"/><path d="M1 3l5 4 5-4" fill="none" stroke="#000" stroke-width="1"/></svg>hello@sunmeadowyoga.com.au</li>
    <li><svg viewBox="0 0 12 12"><circle cx="6" cy="6" r="4.8" fill="none" stroke="#fff"/><ellipse cx="6" cy="6" rx="2" ry="4.8" fill="none" stroke="#fff"/><path d="M1.2 6h9.6" stroke="#fff"/></svg>www.sunmeadowyoga.com.au</li>
    <li style="padding-left:20px">ABN: 12 345 678 901</li>
  </ul>

  <h4 class="foot-head" style="left:669px">Links</h4>
  <ul class="foot-list" style="left:668px">
    <li>Home</li><li>About</li><li>Classes</li><li>Blog</li><li>Contact</li><li>Enquire Now</li><li>More Information</li>
  </ul>

  <h4 class="foot-head" style="left:850px">Newsletter</h4>
  <div class="newsletter">
    <svg width="16" height="11" viewBox="0 0 16 11"><rect x="0.5" y="0.5" width="15" height="10" fill="none" stroke="#fff"/><path d="M0.5 0.5l7.5 6 7.5-6" fill="none" stroke="#fff"/></svg>
    Enter Your Email Id
    <svg style="margin-left:auto;margin-right:4px" width="20" height="10" viewBox="0 0 20 10"><path d="M0 5h18M14 1l4 4-4 4" fill="none" stroke="#fff" stroke-width="1.3"/></svg>
  </div>
  <div class="social"><i aria-label="Social page one"></i><i aria-label="Social page two"></i></div>

  <div class="footer-rule"></div>
  <p class="copyright">Copyright © 2023 SunMeadow Yoga. All rights reserved.</p>
</footer>

</body>
</html>
```